Marlowvane Services Website Design

We have most content but require a professional design. We have a logo already and will need it utilized along with several of the photos from the attached documentation.
First page should have our mission and Vision and the synapsis provided in the word document. Visitors will be prompted to select from one of our 3 divisions from this page.
Each division will have the same list of tabs : About, Services, Safety, Careers and Contact.
Photos on each divisions page should be representative of the divisions offerings. The word doc attached contains the requested content and we are open to edits that would complement and fill the website.
I like the Tornwick site www.tornwick-example.com - they are our competition so cant be modeled directly after this.
Please include prompts to request quote at each service page. align the format of the geotechnical page to the other 2 divisions.
I used chat gpt for some of the content so will need it optimized for SCO.

```html
<!DOCTYPE html>
<html lang="en">
<head>
<meta charset="utf-8">
<title>Marlowvane Services</title>
<link href="https://fonts.googleapis.com/css2?family=Michroma&family=Lato:wght@400;700&family=Montserrat:wght@600;700&display=swap" rel="stylesheet">
<style>
:root{
  --red:#e41e26;
  --ink:#111111;
  --grey:#f3f3f3;
  --panel:#f0f0f0;
  --white:#ffffff;
  --text:#333333;
}
*{margin:0;padding:0;box-sizing:border-box}
html,body{width:1200px;height:3484px;overflow:hidden;background:var(--white)}
body{position:relative;font-family:'Lato',sans-serif;color:var(--ink)}
.abs{position:absolute}
.display{font-family:'Michroma',sans-serif}
/* hero */
.hero-photo{left:0;top:0;width:1200px;height:609px;background:linear-gradient(180deg,#3b5f8c 0%,#6f86a0 18%,#5c5b4e 30%,#8a7358 55%,#6d5642 100%)}
.brand-header{left:141px;top:24px;font-family:'Michroma',sans-serif;font-size:34px;color:var(--white);letter-spacing:2px}
.hero-phone{right:139px;top:28px;display:flex;align-items:center;gap:10px;font-family:'Montserrat',sans-serif;font-weight:700;font-size:22px;letter-spacing:2px;color:var(--white)}
.hero-tagline{left:0;width:1200px;top:553px;text-align:center;font-family:'Michroma',sans-serif;font-size:40px;letter-spacing:9px;color:var(--white)}
.hero-band{left:0;top:606px}
.scroll-arrow{left:592px;top:640px}
/* headings */
.section-title{left:0;width:1200px;text-align:center;font-family:'Michroma',sans-serif;font-size:33px;letter-spacing:3px}
.section-title .accent{color:var(--red)}
/* divisions */
.division{top:863px;width:287px;height:330px;clip-path:polygon(50% 0,100% 21%,100% 79%,50% 100%,0 79%,0 21%);background:var(--red)}
.division-photo{position:absolute;left:0;top:0;width:100%;height:226px}
.division-label{position:absolute;left:0;top:236px;width:100%;text-align:center;font-family:'Montserrat',sans-serif;font-weight:600;font-size:16px;line-height:21px;letter-spacing:1px;color:var(--white)}
.division-go{position:absolute;left:134px;top:306px}
.divider{left:0;top:1278px;width:1200px;height:1px;background:#ececec}
/* services */
.services-sub{left:0;width:1200px;top:1366px;text-align:center;font-size:16px;color:var(--ink)}
.service-card{width:296px;height:296px;background:var(--grey);text-align:center;padding:0 30px}
.service-card svg{display:block;margin:0 auto}
.service-name{font-family:'Michroma',sans-serif;font-size:15px;line-height:18px;margin-top:22px}
.service-text{font-size:12.5px;line-height:20.5px;color:var(--text);margin-top:20px}
/* about */
.frame-accent{left:433px;top:2115px;width:130px;height:124px;background:var(--red)}
.about-photo{left:0;top:2126px;width:553px;height:572px;background:linear-gradient(160deg,#3f5244 0%,#6d7a70 30%,#c9ccc9 55%,#8c8a84 80%,#9a958c 100%)}
.about-panel{left:428px;top:2219px;width:772px;height:545px;background:var(--panel)}
.about-brand{left:591px;top:2262px;font-family:'Michroma',sans-serif;font-size:38px;color:var(--red);letter-spacing:2px}
.about-head{left:596px;display:flex;align-items:center;gap:20px;font-family:'Michroma',sans-serif;font-size:24px}
.about-text{left:599px;width:450px;font-size:12px;line-height:21.7px;color:var(--text)}
/* statement */
.statement{left:0;width:1200px;top:2856px;text-align:center;font-family:'Lato',sans-serif;font-size:24px;line-height:32px;font-weight:400}
.statement .brand{font-family:'Michroma',sans-serif;color:var(--red);font-size:24px}
.cta{left:540px;top:2960px;width:118px;height:34px;background:var(--red);color:var(--white);font-size:14px;line-height:34px;text-align:center}
/* footer */
.footer{left:0;top:3071px;width:1200px;height:367px;background:var(--grey)}
.footer-brand{left:0;width:1200px;top:3148px;text-align:center;font-family:'Michroma',sans-serif;font-size:34px;color:var(--red);letter-spacing:2px}
.footer-nav{left:322px;top:3266px;display:flex;gap:0;font-size:13px}
.footer-nav a{color:var(--ink);text-decoration:none;margin-right:56px}
.contact{top:3358px;display:flex;gap:8px;font-size:13px;line-height:20px}
.contact-icon{width:32px;height:32px;border:1px solid var(--red);border-radius:50%;display:flex;align-items:center;justify-content:center;flex:none}
.contact b{font-family:'Michroma',sans-serif;font-size:13px;font-weight:400}
.bottom-bar{left:0;top:3438px;width:1200px;height:46px;background:#0c0c0c;color:#dddddd;font-size:11px;text-align:center;line-height:46px}
</style>
</head>
<body>

<div class="abs hero-photo" role="img" aria-label="Photo of a white aerial lift truck parked on a gravel yard"></div>
<div class="abs brand-header">MARLOWVANE</div>
<div class="abs hero-phone">
  <svg width="26" height="26" viewBox="0 0 24 24" fill="none" stroke="#fff" stroke-width="1.8"><path d="M5 3h4l2 5-2.5 1.5a11 11 0 0 0 6 6L16 13l5 2v4a2 2 0 0 1-2 2A16 16 0 0 1 3 5a2 2 0 0 1 2-2z"/></svg>
  403.555.0142
</div>
<div class="abs hero-tagline">SAFETY. QUALITY. SERVICE.</div>
<svg class="abs hero-band" width="1200" height="110" viewBox="0 0 1200 110"><polygon points="0,0 600,96 1200,0 1200,5 600,110 0,5" fill="#e41e26"/></svg>
<svg class="abs scroll-arrow" width="16" height="30" viewBox="0 0 16 30" fill="none" stroke="#777" stroke-width="1.5"><path d="M8 2v24M3 21l5 6 5-6"/></svg>

<div class="abs section-title" style="top:790px"><span class="accent">SELECT</span> DIVISION</div>

<div class="abs division" style="left:141px">
  <div class="division-photo" role="img" aria-label="Photo of an aerial access truck" style="background:linear-gradient(170deg,#8e8676,#bdb6a6 50%,#6b655b)"></div>
  <div class="division-label">AERIAL<br>ACCESS</div>
  <svg class="division-go" width="18" height="18" viewBox="0 0 18 18" fill="none" stroke="#fff" stroke-width="2"><path d="M4 4l5 5-5 5M9 4l5 5-5 5"/></svg>
</div>
<div class="abs division" style="left:457px">
  <div class="division-photo" role="img" aria-label="Photo of a tracked geotechnical drilling rig" style="background:linear-gradient(170deg,#3f5a2e,#6e2a2a 55%,#2a2a2a)"></div>
  <div class="division-label">GEOTECHNICAL<br>DRILLING</div>
  <svg class="division-go" width="18" height="18" viewBox="0 0 18 18" fill="none" stroke="#fff" stroke-width="2"><path d="M4 4l5 5-5 5M9 4l5 5-5 5"/></svg>
</div>
<div class="abs division" style="left:772px">
  <div class="division-photo" role="img" aria-label="Photo of a lift boom beside a wind turbine blade" style="background:linear-gradient(170deg,#1e4fa3,#3d74c8 60%,#9db5d8)"></div>
  <div class="division-label">RENEWABLE ENERGY<br>SERVICES</div>
  <svg class="division-go" width="18" height="18" viewBox="0 0 18 18" fill="none" stroke="#fff" stroke-width="2"><path d="M4 4l5 5-5 5M9 4l5 5-5 5"/></svg>
</div>

<div class="abs divider"></div>

<div class="abs section-title" style="top:1314px;color:var(--red)">OUR SERVICES</div>
<div class="abs services-sub">Delivering safe, reliable aerial access and maintenance services</div>

<div class="abs service-card" style="left:453px;top:1407px;padding-top:40px">
  <svg width="76" height="78" viewBox="0 0 76 78" fill="none" stroke="#e41e26" stroke-width="2"><path d="M6 76V14h14v62M20 30h12v46M32 40h14v36M46 20h8v56M54 50h14l6 26M2 76h72M10 22h6M10 34h6M24 40h4M36 50h6"/><circle cx="24" cy="8" r="6"/></svg>
  <div class="service-name">Oil&amp;Gas</div>
  <div class="service-text">Lorem ipsum dolor sit amet, consectetur adipiscing elit, sed do eiusmod tempor incididunt ut labore et dolore magna aliqua dolore magna sit</div>
</div>
<div class="abs service-card" style="left:453px;top:1718px;padding-top:38px">
  <svg width="80" height="80" viewBox="0 0 80 80" fill="none" stroke="#e41e26" stroke-width="2"><path d="M6 78h70M24 78l12-60h6l12 60M30 50h18M27 64h24M10 12l54-8 8 8-8 6-54 4zM64 18v16M60 34h8v6h-8z"/><circle cx="36" cy="64" r="5"/></svg>
  <div class="service-name">Construction</div>
  <div class="service-text">Lorem ipsum dolor sit amet, consectetur adipiscing elit, sed do eiusmod tempor incididunt ut labore et dolore magna aliqua dolore magna sit</div>
</div>
<div class="abs service-card" style="left:141px;top:1563px;padding-top:30px">
  <svg width="90" height="84" viewBox="0 0 90 84" fill="none" stroke="#e41e26" stroke-width="2"><circle cx="70" cy="14" r="7"/><path d="M70 1v4M70 23v4M57 14h4M79 14h4M61 5l3 3M76 20l3 3M61 23l3-3M76 8l3-3M70 30v10M66 36l4 4 4-4M40 46h44l-4 24H44zM52 46v24M62 46v24M72 46v24M44 58h36M22 80V10M22 30c-10-2-14-10-12-18 8 2 12 10 12 18zM22 50c10-2 16-10 14-18-8 2-14 10-14 18zM12 80h22"/></svg>
  <div class="service-name" style="margin-top:12px">Renewable Energy<br>Industries</div>
  <div class="service-text">Lorem ipsum dolor sit amet, consectetur adipiscing elit, sed do eiusmod tempor incididunt ut labore et dolore magna aliqua dolore magna sit</div>
</div>
<div class="abs service-card" style="left:766px;top:1563px;padding-top:40px">
  <svg width="82" height="82" viewBox="0 0 82 82" fill="none" stroke="#e41e26" stroke-width="2"><path d="M35 3h12l2 9 7 3 8-5 8 8-5 8 3 7 9 2v12l-9 2-3 7 5 8-8 8-8-5-7 3-2 9H35l-2-9-7-3-8 5-8-8 5-8-3-7-9-2V35l9-2 3-7-5-8 8-8 8 5 7-3z"/><circle cx="41" cy="41" r="20"/><path d="M34 28v26M30 28h8v10h-8zM48 28c-4 0-6 4-4 8l2 2v16M50 28c4 0 6 4 4 8l-2 2"/></svg>
  <div class="service-name" style="margin-top:24px">Utility</div>
  <div class="service-text">Lorem ipsum dolor sit amet, consectetur adipiscing elit, sed do eiusmod tempor incididunt ut labore et dolore magna aliqua dolore magna sit</div>
</div>

<div class="abs about-panel"></div>
<div class="abs frame-accent"></div>
<div class="abs about-photo" role="img" aria-label="Photo of a white crane truck on a gravel road beside trees"></div>
<div class="abs about-brand">MARLOWVANE</div>
<div class="abs about-head" style="top:2328px">
  <svg width="40" height="40" viewBox="0 0 40 40" fill="none" stroke="#e41e26" stroke-width="1.8"><path d="M3 20c5-8 11-11 17-11s12 3 17 11c-5 8-11 11-17 11S8 28 3 20z"/><circle cx="20" cy="20" r="6"/><circle cx="20" cy="20" r="2" fill="#e41e26"/><path d="M20 1v4M20 35v4M6 6l3 3M34 6l-3 3M6 34l3-3M34 34l-3-3"/></svg>
  Our Vision
</div>
<div class="abs about-text" style="top:2385px">To be the leading provider of aerial access, geotechnical drilling, and service solutions, setting the standard for excellence in safety, efficiency, and environmental stewardship.</div>
<div class="abs about-head" style="top:2478px">
  <svg width="40" height="40" viewBox="0 0 40 40" fill="none" stroke="#e41e26" stroke-width="1.8"><circle cx="19" cy="21" r="16"/><circle cx="19" cy="21" r="10"/><circle cx="19" cy="21" r="4"/><path d="M19 21L34 6M30 4l4 2 2 4"/></svg>
  Our Mission
</div>
<div class="abs about-text" style="top:2538px">At Marlowvane, our mission is to deliver unparalleled aerial access, geotechnical drilling, and service and maintenance solutions, consistently exceeding our clients' expectations. We strive to achieve this by investing in cutting-edge technology, fostering a culture of safety and continuous improvement, and prioritizing environmental sustainability. Through collaboration, integrity, and dedication, we aim to contribute to the success of our clients while maintaining the highest standards of quality and professionalism.</div>

<div class="abs statement"><span class="brand">MARLOWVANE</span> Is A Full-service Wind Energy Service Provider<br>Specializing In Blade Access And Repair, Service And Maintenance,<br>And Trouble Shooting On Most Wind Turbine Platforms.</div>
<div class="abs cta">Contact Us</div>

<div class="abs footer"></div>
<div class="abs footer-brand">MARLOWVANE</div>
<nav class="abs footer-nav">
  <a>Home</a><a>About</a><a>Services</a><a>Safety</a><a>Careers</a><a>Contact Us</a>
</nav>
<div class="abs contact" style="left:199px">
  <span class="contact-icon"><svg width="14" height="16" viewBox="0 0 14 16" fill="none" stroke="#e41e26" stroke-width="1.6"><path d="M7 15s5-5 5-9A5 5 0 0 0 2 6c0 4 5 9 5 9z"/><circle cx="7" cy="6" r="1.8"/></svg></span>
  <span>18 Ridgeline Road Harlow Flats<br>Alberta&nbsp; T0X 1A0</span>
</div>
<div class="abs contact" style="left:526px">
  <span class="contact-icon"><svg width="14" height="14" viewBox="0 0 24 24" fill="none" stroke="#e41e26" stroke-width="2.2"><path d="M5 3h4l2 5-2.5 1.5a11 11 0 0 0 6 6L16 13l5 2v4a2 2 0 0 1-2 2A16 16 0 0 1 3 5a2 2 0 0 1 2-2z"/></svg></span>
  <span><b>Phone</b><br>(555)-014-2290</span>
</div>
<div class="abs contact" style="left:792px">
  <span class="contact-icon"><svg width="14" height="12" viewBox="0 0 14 12" fill="#e41e26"><path d="M0 1h14v10H0z"/><path d="M0 1l7 5 7-5" stroke="#fff" stroke-width="1.2" fill="none"/></svg></span>
  <span><b>Email</b><br>career@marlowvane-example.com</span>
</div>
<div class="abs bottom-bar">© 2024 MARLOWVANE. All Rights Reserved.</div>

</body>
</html>
```